SunGrove Yoga Website Design

Business Logo - attached
5 pages being:
Home
About
Classes
Blog
Contact

Would like Scrolling webpage and yoga symbols to be used.

Must have's being:
Easy to navigate, Text needs to be able to be edited/updated, Enquire Now Links, More Information Links, be a secure site, SEO,

Please refer to attached document for the information for the body of the website.

Target Market(s)

Educators, Community Service, Health and Wellbeing, Mental Health

Industry/Entity Type

Yoga

Coding

Coded - Design and coding required

Number of Pages Required

5+ page

Font styles to use
Other font styles liked:
• Bella Bold BC

Colors
0094D4
00A9DD
6FCCEA
C7EBF8
E9F6FB
6B429C
8869AF
B7A5CE
E3DAEB
F3F0F8

Requirements
Must have
• Easy to navigate, Text needs to be able to be edited/updated, Enquire Now Links, More Information Links, be a secure site, SEO,
Nice to have
• Scrolling webpage, yoga symbols

```html
<!DOCTYPE html>
<html lang="en">
<head>
<meta charset="utf-8">
<title>SunGrove Yoga – Home</title>
<link href="https://fonts.googleapis.com/css2?family=Caveat+Brush&family=Poppins:wght@400;500;600;700&family=Tinos&display=swap" rel="stylesheet">
<style>
:root{
  --purple:#6b2fd1;
  --purple-deep:#5a2cb8;
  --violet:#8b5ad8;
  --lilac:#b7a5ce;
  --mist:#f3f0f8;
  --ink:#1a1a1a;
  --white:#ffffff;
  --black:#000000;
}
*{box-sizing:border-box;margin:0;padding:0}
html,body{width:1200px;height:3932px;overflow:hidden;background:var(--white)}
body{position:relative;font-family:"Poppins",sans-serif;color:var(--ink)}
.abs{position:absolute}
.display{font-family:"Caveat Brush",cursive;font-weight:400;letter-spacing:1px}

/* header */
.top-strip{top:0;left:0;width:1200px;height:12px;background:linear-gradient(90deg,#7b3fb8,#9a4fc4)}
.site-header{top:12px;left:0;width:1200px;height:173px;background:var(--white)}
.nav-link{font-size:20px;color:#222;top:105px}
.brand{top:95px;left:505px;width:200px;text-align:center;font-size:20px;font-weight:600;color:var(--purple)}
.brand-dot{top:52px;left:591px;width:28px;height:28px;border-radius:50%;background:var(--purple)}
.search{top:104px;left:1024px}

/* hero */
.hero{top:185px;left:0;width:1200px;height:770px;background:linear-gradient(180deg,#3a2a8a 0%,#7a55b8 28%,#c77fc0 48%,#a45fb8 62%,#6f3fa0 100%)}
.hero-curve{top:760px;left:0}
.hero-title{top:350px;left:600px;font-size:62px;line-height:70px;color:var(--white)}
.hero-text{top:510px;left:600px;width:490px;font-size:14px;line-height:31px;color:var(--white);text-align:justify}
.slider-dots{top:778px;left:560px;display:flex;gap:3px}
.slider-dots span{width:25px;height:25px;border-radius:50%;background:var(--white)}
.slider-dots span:first-child{background:var(--black)}

/* buttons */
.btn{display:flex;height:50px;border-radius:8px;overflow:hidden;box-shadow:0 2px 6px rgba(0,0,0,.18)}
.btn-label{display:flex;align-items:center;justify-content:center;width:140px;font-size:15px;font-weight:600;letter-spacing:.3px}
.btn-mark{display:flex;align-items:center;justify-content:center;width:58px;border:2px solid #e3daeb;border-left:none}
.btn-mark i{width:22px;height:22px;border-radius:50%;border:2px solid currentColor}
.btn-solid .btn-label{background:var(--purple);color:var(--white)}
.btn-solid .btn-mark{background:var(--white);color:var(--violet)}
.btn-light .btn-label{background:var(--white);color:#222}
.btn-light .btn-mark{background:var(--purple);color:var(--white);border-color:var(--purple)}

/* about */
.about-title{top:1018px;left:110px;font-size:46px;color:#111}
.about-title span{color:var(--purple)}
.about-text{top:1080px;left:110px;width:446px;font-size:16px;line-height:31px;text-align:justify;color:#222}
.about-photo{top:1100px;left:645px;width:420px;height:410px;border-radius:50%;border-right:6px solid var(--violet);padding:6px}
.about-photo div{width:100%;height:100%;border-radius:50%;background:linear-gradient(135deg,#d8d4cc,#9c8f86 55%,#5c6a5a)}

/* benefits */
.benefits{top:1663px;left:0;width:1200px;height:1529px;background:linear-gradient(180deg,#8a56d6 0%,#9b64d3 30%,#8453c6 60%,#6b3ec0 100%)}
.benefits-title{top:1740px;left:0;width:1200px;text-align:center;font-size:44px;color:var(--white)}
.benefits-intro{top:1806px;left:120px;width:960px;text-align:center;font-size:15.5px;line-height:31px;color:var(--white)}
.photo-card{border:4px solid var(--white);border-radius:110px 4px 110px 4px}
.card-a{top:1915px;left:110px;width:450px;height:311px;background:linear-gradient(135deg,#efe9e2,#d9c8b6 50%,#e45fb1 75%,#6d6f78)}
.card-b{top:2286px;left:657px;width:451px;height:310px;background:linear-gradient(135deg,#e8e4dc,#b9a994 50%,#5d6d8c)}
.card-c{top:2665px;left:110px;width:450px;height:310px;background:linear-gradient(135deg,#f4f1ec,#e6ddd1 55%,#c9b9a6)}
.group-title{font-size:20px;font-weight:600;color:var(--white);letter-spacing:.3px}
.ticks{list-style:none;color:var(--white);font-size:16.5px}
.ticks li{display:flex;align-items:flex-start;gap:16px}
.ticks svg{flex:none;margin-top:6px}
.ticks-bodies li{line-height:32.5px}
.ticks-bodies li svg{margin-top:8px}
.ticks-loose li{height:37px}

/* call to action */
.footer-band{top:3352px;left:0;width:1200px;height:580px;background:var(--black)}
.cta-box{top:3277px;left:110px;width:979px;height:202px;background:var(--white);border:2px solid #d6d6d6;border-radius:4px}
.cta-title{top:3318px;left:0;width:1200px;text-align:center;font-size:42px;color:#111}

/* footer */
.footer-brand{top:3606px;left:152px;width:200px;text-align:center;font-size:22px;font-weight:600;color:var(--white)}
.footer-brand-dot{top:3548px;left:232px;width:40px;height:40px;border-radius:50%;border:3px solid var(--white)}
.social{top:3752px;width:26px;height:26px;border-radius:6px;background:var(--white)}
.footer-head{font-size:22px;color:var(--white);top:3530px}
.footer-list{list-style:none;font-size:14px;line-height:31px;color:var(--white);top:3568px}
.contact-row{left:822px;display:flex;align-items:center;gap:12px;font-size:15px;color:var(--white)}
.contact-row .ic{width:30px;height:28px;background:var(--white);border-radius:3px;display:flex;align-items:center;justify-content:center;flex:none}
.footer-rule{top:3853px;left:104px;width:977px;height:1px;background:#777}
.copyright{top:3876px;left:0;width:1200px;text-align:center;font-family:"Tinos",serif;font-size:15px;color:var(--white)}
</style>
</head>
<body>

<div class="abs top-strip"></div>
<header class="abs site-header"></header>
<nav>
  <a class="abs nav-link" style="left:136px">Home</a>
  <a class="abs nav-link" style="left:281px">About</a>
  <a class="abs nav-link" style="left:429px">Classes</a>
  <a class="abs nav-link" style="left:728px;top:102px">Blog</a>
  <a class="abs nav-link" style="left:860px;top:102px">Contact</a>
</nav>
<div class="abs brand-dot"></div>
<div class="abs brand">SunGrove Yoga</div>
<svg class="abs search" width="30" height="30" viewBox="0 0 30 30"><circle cx="12" cy="12" r="9.5" fill="none" stroke="#111" stroke-width="2.8"/><line x1="19" y1="19" x2="28" y2="28" stroke="#111" stroke-width="3" stroke-linecap="round"/></svg>

<section class="abs hero" role="img" aria-label="Photo of a person meditating in a seated yoga pose on a beach at purple sunset"></section>
<svg class="abs hero-curve" width="1200" height="200" viewBox="0 0 1200 200">
  <path d="M0 26 Q600 330 1200 18 L1200 200 L0 200 Z" fill="#ffffff"/>
  <path d="M55 70 Q640 300 1200 20 L1200 34 Q640 330 55 70 Z" fill="#6b2fd1"/>
</svg>
<h1 class="abs display hero-title">WELCOME TO<br>SUNGROVE YOGA</h1>
<p class="abs hero-text">SunGrove Yoga believe that you are never too young to benefit from and fall in love with yoga. My aim is to EMPOWER kids and teens to thrive by teaching life skills in Yoga, Mindfulness and Breathing techniques to deal with daily challenges and big emotions.</p>
<a class="abs btn btn-solid" style="top:646px;left:600px"><span class="btn-label" style="width:140px">GET STARTED</span><span class="btn-mark"><i></i></span></a>
<div class="abs slider-dots"><span></span><span></span><span></span></div>

<h2 class="abs display about-title">ABOUT <span>US</span></h2>
<div class="abs about-text">
  <p>Hi and welcome to SunGrove Yoga!</p>
  <p>My name is Hannah, and I am the creator &amp; facilitator of SunGrove Yoga. With the increasing numbers of youth mental health, I have started SunGrove Yoga wanting to assist children and teens with their mental health for life, with the magic of yoga.</p>
  <p>I had always wanted to teach children, but had never found the right platform to do so… That was until I found yoga! I genuinely believe the practice of yoga and mindfulness especially at a young age can offer life-long tools to kids and teens such as dealing with their emotions, developing resilience, self-awareness, respect and confidence in a positive and fun environment.</p>
</div>
<a class="abs btn btn-solid" style="top:1524px;left:113px"><span class="btn-label">READ MORE</span><span class="btn-mark"><i></i></span></a>
<div class="abs about-photo"><div role="img" aria-label="Photo of a group of women in a yoga class sitting with hands in prayer position"></div></div>

<section class="abs benefits" role="img" aria-label="Soft purple background with a faint silhouette of a meditating figure"></section>
<h2 class="abs display benefits-title">BENEFITS OF YOGA…</h2>
<p class="abs benefits-intro">The benefits of yoga can last a lifetime. It is my aim &amp; passion to introduce yoga to kids of all ages and backgrounds so that they can not only experience the benefits of yoga but fall in love with the practice.</p>

<div class="abs photo-card card-a" role="img" aria-label="Photo of smiling students stretching in a bright yoga studio"></div>
<h3 class="abs group-title" style="top:1900px;left:635px">HEALTHY BODIES:</h3>
<ul class="abs ticks ticks-bodies" style="top:1952px;left:633px;width:500px">
  <li><svg width="18" height="18" viewBox="0 0 18 18"><circle cx="9" cy="9" r="9" fill="#fff"/><path d="M7.5 5.5L11 9l-3.5 3.5" fill="none" stroke="#6b2fd1" stroke-width="2"/></svg>Develops strong, flexible and healthy bodies</li>
  <li><svg width="18" height="18" viewBox="0 0 18 18"><circle cx="9" cy="9" r="9" fill="#fff"/><path d="M7.5 5.5L11 9l-3.5 3.5" fill="none" stroke="#6b2fd1" stroke-width="2"/></svg>Promotes spinal alignment and good posture</li>
  <li><svg width="18" height="18" viewBox="0 0 18 18"><circle cx="9" cy="9" r="9" fill="#fff"/><path d="M7.5 5.5L11 9l-3.5 3.5" fill="none" stroke="#6b2fd1" stroke-width="2"/></svg>Builds energy and stamina</li>
  <li><svg width="18" height="18" viewBox="0 0 18 18"><circle cx="9" cy="9" r="9" fill="#fff"/><path d="M7.5 5.5L11 9l-3.5 3.5" fill="none" stroke="#6b2fd1" stroke-width="2"/></svg>Improves internal physical function – organs, digestion, elimination, circulation, and blood flow.</li>
  <li><svg width="18" height="18" viewBox="0 0 18 18"><circle cx="9" cy="9" r="9" fill="#fff"/><path d="M7.5 5.5L11 9l-3.5 3.5" fill="none" stroke="#6b2fd1" stroke-width="2"/></svg>Helps breathing and lung capacity</li>
  <li><svg width="18" height="18" viewBox="0 0 18 18"><circle cx="9" cy="9" r="9" fill="#fff"/><path d="M7.5 5.5L11 9l-3.5 3.5" fill="none" stroke="#6b2fd1" stroke-width="2"/></svg>Teaches the enjoyment of movement</li>
  <li><svg width="18" height="18" viewBox="0 0 18 18"><circle cx="9" cy="9" r="9" fill="#fff"/><path d="M7.5 5.5L11 9l-3.5 3.5" fill="none" stroke="#6b2fd1" stroke-width="2"/></svg>Works the ‘whole’ body</li>
</ul>

<h3 class="abs group-title" style="top:2280px;left:110px">HEALTHY MINDS</h3>
<ul class="abs ticks ticks-loose" style="top:2332px;left:110px;width:500px">
  <li><svg width="18" height="18" viewBox="0 0 18 18"><circle cx="9" cy="9" r="9" fill="#fff"/><path d="M7.5 5.5L11 9l-3.5 3.5" fill="none" stroke="#6b2fd1" stroke-width="2"/></svg>Cultivates confidence and self-esteem</li>
  <li><svg width="18" height="18" viewBox="0 0 18 18"><circle cx="9" cy="9" r="9" fill="#fff"/><path d="M7.5 5.5L11 9l-3.5 3.5" fill="none" stroke="#6b2fd1" stroke-width="2"/></svg>Develops concentration and attention</li>
  <li><svg width="18" height="18" viewBox="0 0 18 18"><circle cx="9" cy="9" r="9" fill="#fff"/><path d="M7.5 5.5L11 9l-3.5 3.5" fill="none" stroke="#6b2fd1" stroke-width="2"/></svg>Clears the mind for better clarity and decision making</li>
  <li><svg width="18" height="18" viewBox="0 0 18 18"><circle cx="9" cy="9" r="9" fill="#fff"/><path d="M7.5 5.5L11 9l-3.5 3.5" fill="none" stroke="#6b2fd1" stroke-width="2"/></svg>Helps relax and sleep better</li>
  <li><svg width="18" height="18" viewBox="0 0 18 18"><circle cx="9" cy="9" r="9" fill="#fff"/><path d="M7.5 5.5L11 9l-3.5 3.5" fill="none" stroke="#6b2fd1" stroke-width="2"/></svg>Calms the nervous system</li>
  <li><svg width="18" height="18" viewBox="0 0 18 18"><circle cx="9" cy="9" r="9" fill="#fff"/><path d="M7.5 5.5L11 9l-3.5 3.5" fill="none" stroke="#6b2fd1" stroke-width="2"/></svg>Learns to cope with stressful situations</li>
  <li><svg width="18" height="18" viewBox="0 0 18 18"><circle cx="9" cy="9" r="9" fill="#fff"/><path d="M7.5 5.5L11 9l-3.5 3.5" fill="none" stroke="#6b2fd1" stroke-width="2"/></svg>Balances emotions</li>
</ul>
<div class="abs photo-card card-b" role="img" aria-label="Photo of a mixed-age group laughing together during a seated yoga class"></div>

<div class="abs photo-card card-c" role="img" aria-label="Photo of a parent and child doing a downward dog pose together beside a plant"></div>
<h3 class="abs group-title" style="top:2650px;left:638px">HEALTHY SPIRITS</h3>
<ul class="abs ticks ticks-loose" style="top:2703px;left:633px;width:500px">
  <li><svg width="18" height="18" viewBox="0 0 18 18"><circle cx="9" cy="9" r="9" fill="#fff"/><path d="M7.5 5.5L11 9l-3.5 3.5" fill="none" stroke="#6b2fd1" stroke-width="2"/></svg>Fosters creativity, expression and imagination</li>
  <li><svg width="18" height="18" viewBox="0 0 18 18"><circle cx="9" cy="9" r="9" fill="#fff"/><path d="M7.5 5.5L11 9l-3.5 3.5" fill="none" stroke="#6b2fd1" stroke-width="2"/></svg>Cultivates kindness to themselves and others</li>
  <li><svg width="18" height="18" viewBox="0 0 18 18"><circle cx="9" cy="9" r="9" fill="#fff"/><path d="M7.5 5.5L11 9l-3.5 3.5" fill="none" stroke="#6b2fd1" stroke-width="2"/></svg>Cultivates respect for self and others</li>
  <li><svg width="18" height="18" viewBox="0 0 18 18"><circle cx="9" cy="9" r="9" fill="#fff"/><path d="M7.5 5.5L11 9l-3.5 3.5" fill="none" stroke="#6b2fd1" stroke-width="2"/></svg>Builds balance and inner quiet</li>
  <li><svg width="18" height="18" viewBox="0 0 18 18"><circle cx="9" cy="9" r="9" fill="#fff"/><path d="M7.5 5.5L11 9l-3.5 3.5" fill="none" stroke="#6b2fd1" stroke-width="2"/></svg>Builds inner strength and resilience</li>
  <li><svg width="18" height="18" viewBox="0 0 18 18"><circle cx="9" cy="9" r="9" fill="#fff"/><path d="M7.5 5.5L11 9l-3.5 3.5" fill="none" stroke="#6b2fd1" stroke-width="2"/></svg>Teaches self-awareness</li>
  <li><svg width="18" height="18" viewBox="0 0 18 18"><circle cx="9" cy="9" r="9" fill="#fff"/><path d="M7.5 5.5L11 9l-3.5 3.5" fill="none" stroke="#6b2fd1" stroke-width="2"/></svg>Focuses on positive self-talk</li>
</ul>
<a class="abs btn btn-light" style="top:3039px;left:498px"><span class="btn-label">READ MORE</span><span class="btn-mark"><i></i></span></a>

<div class="abs footer-band"></div>
<div class="abs cta-box"></div>
<h2 class="abs display cta-title">DO YOU HAVE ANY DOUBYTS ?</h2>
<a class="abs btn btn-solid" style="top:3389px;left:498px"><span class="btn-label">CONTACT US</span><span class="btn-mark"><i></i></span></a>

<footer>
  <div class="abs footer-brand-dot"></div>
  <div class="abs footer-brand">SunGrove Yoga</div>
  <div class="abs social" style="left:214px" role="img" aria-label="Social link"></div>
  <div class="abs social" style="left:255px" role="img" aria-label="Social link"></div>

  <h4 class="abs display footer-head" style="left:420px">QUICK LINKS</h4>
  <ul class="abs footer-list" style="left:420px">
    <li>Home</li><li>About</li><li>Classes</li><li>Blog</li><li>Contact</li>
  </ul>
  <h4 class="abs display footer-head" style="left:583px">OTHER LINKS</h4>
  <ul class="abs footer-list" style="left:583px">
    <li>Enquire Now</li><li>More Information</li><li>Privacy Policy</li><li>Terms &amp; Conditions</li>
  </ul>
  <h4 class="abs display footer-head" style="left:817px;top:3524px">GET IN TOUCH</h4>

  <div class="abs contact-row" style="top:3576px;font-size:14px;line-height:22px"><span class="ic"><svg width="16" height="18" viewBox="0 0 16 18"><path d="M8 1a5 5 0 0 0-5 5c0 4 5 9 5 9s5-5 5-9a5 5 0 0 0-5-5z" fill="#111"/><circle cx="8" cy="6" r="2" fill="#fff"/></svg></span><span>Fernvale, Victoria<br>Australia 3799</span></div>
  <div class="abs contact-row" style="top:3627px"><span class="ic"><svg width="18" height="18" viewBox="0 0 24 24"><path d="M6.6 10.8a15 15 0 0 0 6.6 6.6l2.2-2.2a1 1 0 0 1 1-.25 11.4 11.4 0 0 0 3.6.57 1 1 0 0 1 1 1V20a1 1 0 0 1-1 1A17 17 0 0 1 3 4a1 1 0 0 1 1-1h3.5a1 1 0 0 1 1 1c0 1.250.2 2.450.57 3.57a1 1 0 0 1-.25 1z" fill="#111"/></svg></span>0400 555 218</div>
  <div class="abs contact-row" style="top:3674px"><span class="ic"><svg width="20" height="16" viewBox="0 0 20 16"><rect x="1" y="1" width="18" height="14" fill="none" stroke="#111" stroke-width="2"/><path d="M1 1l9 8 9-8" fill="none" stroke="#111" stroke-width="2"/></svg></span>info@sungroveyoga.example</div>
  <div class="abs contact-row" style="top:3721px"><span class="ic"><svg width="20" height="20" viewBox="0 0 20 20"><circle cx="10" cy="10" r="8.5" fill="none" stroke="#111" stroke-width="1.8"/><ellipse cx="10" cy="10" rx="3.8" ry="8.5" fill="none" stroke="#111" stroke-width="1.5"/><path d="M1.5 10h17M3 5.5h14M3 14.5h14" stroke="#111" stroke-width="1.5"/></svg></span>www.sungroveyoga.example</div>
  <div class="abs contact-row" style="top:3760px;font-size:13.5px"><span class="ic"></span>ABN:&nbsp; 12 345 678 901</div>

  <div class="abs footer-rule"></div>
  <p class="abs copyright">Copyright 2023 SunGrove Yoga</p>
</footer>

</body>
</html>
```